Business Card Design needed for logo design project

Our company needs a Business Card Design. Please refer to our original project in the link above.
Dorian Pellworth
Broker

W: Velvetcrestestates.example
P: 555-302-7184
F: 555-741-2096
E: dorianpellworth@mailbox.example
A: North Dallas Office
Updates

Name Spelling update , sorry Dorian Pellworth card is double sided

```html
<!DOCTYPE html>
<html lang="en">
<head>
<meta charset="utf-8">
<title>Dorian Pellworth – Business Card</title>
<link rel="stylesheet" href="https://fonts.googleapis.com/css2?family=Open+Sans:wght@400;600;700&display=swap">
<style>
  :root {
    --stage: #e9e8e6;
    --card: #ffffff;
    --card-back: #f4f4f2;
    --gold: #a88a5c;
    --gold-soft: #e8ddcc;
    --gold-faint: #efe7da;
    --green: #3fb57a;
    --green-soft: #cfeee0;
    --grey: #9a9a9a;
  }
  * { box-sizing: border-box; margin: 0; padding: 0; }
  html, body { width: 1200px; height: 800px; overflow: hidden; }
  body {
    background: var(--stage);
    font-family: "Open Sans", Arial, sans-serif;
    display: flex;
    flex-direction: column;
    align-items: center;
    justify-content: center;
    gap: 40px;
  }
  .card {
    width: 525px;
    height: 300px;
    position: relative;
    overflow: hidden;
    box-shadow: 0 6px 18px rgba(0,0,0,0.12);
  }
  .card--front {
    background: var(--card);
    display: flex;
    align-items: center;
    justify-content: center;
  }
  .brand {
    display: flex;
    align-items: center;
    gap: 12px;
  }
  .brand__mark {
    width: 22px;
    height: 22px;
    background: var(--gold);
  }
  .brand__name {
    font-size: 24px;
    font-weight: 600;
    color: var(--gold);
    letter-spacing: 2px;
    text-transform: uppercase;
  }
  .card--back { background: var(--card-back); }
  .deco-shape {
    position: absolute;
    border-radius: 50%;
    background: var(--gold-faint);
  }
  .deco-shape--left { width: 260px; height: 260px; left: -150px; top: 150px; }
  .deco-shape--right { width: 260px; height: 260px; right: -90px; top: -150px; }
  .deco-laurel {
    position: absolute;
    border-radius: 60px;
    background: linear-gradient(160deg, var(--green-soft), rgba(207,238,224,0.3));
  }
  .deco-laurel--upright { left: 160px; top: 40px; width: 70px; height: 240px; }
  .deco-laurel--sweep { left: 290px; top: 60px; width: 210px; height: 70px; transform: rotate(18deg); }
  .holder {
    position: absolute;
    left: 190px;
    top: 52px;
  }
  .holder__name {
    font-size: 17px;
    font-weight: 700;
    color: var(--gold);
  }
  .holder__role {
    font-size: 10px;
    color: var(--grey);
  }
  .contact {
    position: absolute;
    left: 265px;
    top: 135px;
    list-style: none;
    font-size: 12.5px;
    color: var(--gold);
    line-height: 24px;
  }
</style>
</head>
<body>
  <section class="card card--front">
    <div class="brand">
      <span class="brand__mark"></span>
      <span class="brand__name">Velvetcrest Estates</span>
    </div>
  </section>

  <section class="card card--back">
    <div class="deco-shape deco-shape--left"></div>
    <div class="deco-shape deco-shape--right"></div>
    <div class="deco-laurel deco-laurel--upright" role="img" aria-label="Faint green laurel branch"></div>
    <div class="deco-laurel deco-laurel--sweep" role="img" aria-label="Faint green laurel branch"></div>
    <div class="holder">
      <p class="holder__name">Dorian Pellworth</p>
      <p class="holder__role">Broker</p>
    </div>
    <ul class="contact">
      <li>P: 555-302-7184</li>
      <li>F: 555-741-2096</li>
      <li>W: Velvetcrestestates.example</li>
      <li>E: dorianpellworth@mailbox.example</li>
    </ul>
  </section>
</body>
</html>
```